Create a Graphic About YOURSELF and PixelHarbor

PixelHarbor would like you (designers) to create an awesome graphic to promote YOURSELF and your profile on PixelHarbor!

Your graphic should communicate your name, your services and should mention PixelHarbor.

The design should be perfect for sharing on Chatterly. Here's an example of what we'd like http://blog.pixelharbor-example.ca/article/333/pixelharbor-launches-3000-hire-me-social-design-contest

Once you submitted your design, we'd love you to share the design ('advertisement') and promote yourself and PixelHarbor to your friends and potential customers. So make your submissions great and get your friends to vote for your design by 'Liking' it on Chatterly!

Prizes:
$1500 - "PixelHarbor Community" prize awarded to the designer with the most Chatterly 'Likes'
5 x $50 for the next 5 'most liked' designs on Chatterly

$1000 - "Hire Me" prize awarded to the designer who receives the most client invites
5 x $50 for the next 5 'most invited' designers

In summary, this is a great opportunity for you to increase your exposure to PixelHarbor customers and win cash prizes. Show off your design skills and get hired by PixelHarbor customers from around the world!

Target Market(s)

Fans, friends and customers of YOU

Industry/Entity Type

Cash

Requirements
Must have
• 1) Include your PixelHarbor user name on the graphic so customers can find you in the PixelHarbor Designer Directory
2) Include the tagline "Hire Me on PixelHarbor.com!" in your graphic design.
3) Share your design's URL on our Chatterly wall at http://chatterly-example.com/pixelharbor and get your friends to 'like' your design.
Nice to have
• 1) Include a tagline that expresses your design approach/philosophy
2) Artwork dimensions: 403 x 403 px
3) You can submit more than 1 design!
Should not have
• You must own the copyright of any images you use including stock imagery.

```html
<!DOCTYPE html>
<html lang="en">
<head>
<meta charset="utf-8">
<title>Hire Me – Mara Lindt, Design and Direction</title>
<link href="https://fonts.googleapis.com/css2?family=Oswald:wght@300;400;500&family=Yellowtail&family=Kanit:ital,wght@1,600&display=swap" rel="stylesheet">
<style>
  :root {
    --paper: #fde1c2;
    --paper-edge: #f8cf9e;
    --ink: #2b2724;
    --ribbon: #fbcb8e;
    --ribbon-dark: #f6b466;
    --border-dot: #e9a24f;
  }
  * { margin: 0; padding: 0; box-sizing: border-box; }
  html, body { width: 1200px; height: 1200px; overflow: hidden; }
  body {
    background: radial-gradient(ellipse at center, var(--paper) 60%, var(--paper-edge) 100%);
    color: var(--ink);
    font-family: "Oswald", sans-serif;
    position: relative;
  }
  .frame {
    position: absolute; inset: 6px;
    border: 2px dotted var(--border-dot);
  }
  .mark { position: absolute; left: 0; top: 0; }
  .mark-name {
    position: absolute; left: 500px; width: 200px; top: 258px;
    text-align: center; font-family: "Oswald", sans-serif; font-weight: 500;
    font-size: 30px; letter-spacing: 3px; line-height: 1;
  }
  .services {
    position: absolute; left: 500px; width: 200px; top: 340px;
    text-align: center; color: var(--paper);
    font-family: "Kanit", sans-serif; font-style: italic; font-weight: 600;
    font-size: 12px; letter-spacing: 1.5px;
  }
  .services .joiner { font-family: "Yellowtail", cursive; font-style: normal; font-weight: 400; font-size: 11px; letter-spacing: 0; margin: 0 3px; }
  .rule { position: absolute; left: 498px; width: 208px; border-top: 1px solid var(--ink); }
  .tagline { position: absolute; left: 450px; width: 300px; text-align: center; white-space: nowrap; line-height: 1; }
  .t-making { top: 408px; font-size: 80px; font-weight: 400; letter-spacing: 2px; }
  .t-the { top: 488px; font-family: "Yellowtail", cursive; font-size: 34px; }
  .t-world { top: 530px; font-size: 84px; font-weight: 400; letter-spacing: 2px; }
  .t-beautiful { top: 614px; font-size: 54px; font-weight: 300; letter-spacing: 0.5px; }
  .t-one {
    top: 658px; font-size: 146px; font-weight: 500; letter-spacing: 2px;
    color: transparent; -webkit-text-stroke: 9px var(--ink);
  }
  .t-layer { top: 786px; font-size: 96px; font-weight: 400; letter-spacing: 2px; }
  .t-time { top: 874px; font-size: 52px; font-weight: 300; letter-spacing: 5px; }
  .ribbon { position: absolute; left: 0; top: 0; }
  .hire {
    position: absolute; left: 340px; width: 520px; top: 1006px;
    text-align: center; transform: rotate(-0.6deg);
    font-family: "Kanit", sans-serif; font-style: italic; font-weight: 600;
    font-size: 20px; letter-spacing: 1.5px;
  }
  .hire .joiner { font-family: "Yellowtail", cursive; font-style: normal; font-weight: 400; font-size: 22px; letter-spacing: 0; }
  .portfolio {
    position: absolute; left: 300px; width: 600px; top: 1142px;
    text-align: center; font-size: 15px; font-weight: 400; letter-spacing: 0.5px;
  }
</style>
</head>
<body>
  <div class="frame"></div>

  <svg class="mark" width="1200" height="400" viewBox="0 0 1200 400" aria-hidden="true">
    <circle cx="600" cy="200" r="92" fill="none" stroke="var(--ink)" stroke-width="1.5"/>
    <polygon points="497,322 703,322 690,345 706,368 494,368 510,345" fill="var(--ink)"/>
  </svg>
  <div class="mark-name">MARA</div>
  <div class="services">DESIGN <span class="joiner">and</span> DIRECTION</div>

  <div class="rule" style="top:385px"></div>
  <div class="rule" style="top:392px"></div>

  <div class="tagline t-making">MAKING</div>
  <div class="tagline t-the">- The -</div>
  <div class="tagline t-world">WORLD</div>
  <div class="tagline t-beautiful">BEAUTIFUL</div>
  <div class="tagline t-one">ONE</div>
  <div class="tagline t-layer">LAYER</div>
  <div class="tagline t-time">AT A TIME.</div>

  <div class="rule" style="top:934px"></div>
  <div class="rule" style="top:941px"></div>

  <svg class="ribbon" width="1200" height="1200" viewBox="0 0 1200 1200" aria-hidden="true">
    <g fill="var(--ribbon)" stroke="var(--ribbon-dark)" stroke-width="2" opacity="0.9">
      <polygon points="820,948 918,944 874,980 910,1010 828,1012"/>
      <polygon points="286,1026 370,1026 376,1090 280,1088 320,1056"/>
      <polygon points="820,948 860,984 828,1012" fill="var(--ribbon-dark)"/>
      <polygon points="330,1026 370,1026 376,1060" fill="var(--ribbon-dark)"/>
      <polygon points="340,984 860,982 858,1050 330,1058"/>
    </g>
  </svg>
  <div class="hire">HIRE ME ON PIXELHARBOR <span class="joiner">at</span> MARAFORKS</div>

  <div class="portfolio">FOLIOYARD-EXAMPLE.COM/MARALINDT</div>
</body>
</html>
```